Business card and stationery for an eCommerce store
Vornel Home Solutions
Business card and stationery for an eCommerce store - Retailers
Creative Brief
Simple
Tarin Velo K.M
Managing Partner
Vornel Home Solutions #254 , 6th B Cross, G D Layout, Hosadiga Ext, Kelnavadi, Bangalore - 560481
pkelmandro@vomta.in
www.vomta.in
Vornel Home Solutions is the private limited firm that owns vomta.in. Vornel Home Solutions doesn't have any separate identity/ logo created. In addition to business card design, I would also like to see designs for Letterhead and Envelope.
Concepts
Business Cards/Letterhead/ Envelopes/Notepads/Tshirt/labels for copper kite crate

```html
<!DOCTYPE html>
<html lang="en">
<head>
<meta charset="utf-8">
<title>Vornel Home Solutions – Stationery</title>
<link href="https://fonts.googleapis.com/css2?family=Roboto:wght@400;700;900&display=swap" rel="stylesheet">
<style>
:root{
  --stage:#000;
  --paper:#fff;
  --orange:#f39a1e;
  --orange-deep:#e8731b;
  --red:#b81f2e;
  --ink:#fff;
  --brand-font:"Roboto", Arial, sans-serif;
}
*{box-sizing:border-box;margin:0;padding:0}
html,body{width:1200px;height:768px;overflow:hidden;background:var(--stage)}
.canvas{position:relative;width:1200px;height:768px;font-family:var(--brand-font)}
.piece{position:absolute;overflow:hidden}
.brand{position:absolute;display:flex;align-items:center;gap:6px;font-weight:900;color:var(--orange-deep);letter-spacing:-.5px;white-space:nowrap}
.brand .mark{display:inline-block;background:var(--orange-deep)}
.wave{position:absolute;left:0;bottom:0;width:100%}
.address{position:absolute;color:var(--ink);font-size:9px;line-height:13px}
.letterhead{left:48px;top:60px;width:506px;height:650px;background:var(--paper)}
.letterhead .brand{left:26px;top:34px;font-size:40px}
.letterhead .brand .mark{width:14px;height:14px}
.letterhead .address{left:22px;bottom:12px;line-height:12px}
.card-front{left:576px;top:58px;width:278px;height:122px;background:var(--paper);border-radius:10px}
.card-front .brand{left:12px;top:14px;font-size:24px}
.card-front .brand .mark{width:9px;height:9px}
.card-front .person{position:absolute;right:16px;top:36px;text-align:center;font-size:8px;color:var(--orange-deep);line-height:11px}
.card-front .person strong{font-weight:700}
.card-front .address{left:10px;bottom:10px;font-size:6.5px;line-height:9px}
.card-back{left:878px;top:96px;width:276px;height:120px;background:var(--paper);border-radius:10px}
.card-orange{left:655px;top:209px;width:207px;height:115px;background:var(--orange);border-radius:10px}
.card-red{left:910px;top:257px;width:208px;height:115px;background:var(--red);border-radius:10px}
.card-back .brand,.card-orange .brand,.card-red .brand{left:50%;top:50%;transform:translate(-50%,-50%);font-size:28px}
.card-orange .brand,.card-red .brand{color:var(--ink)}
.card-orange .brand .mark,.card-red .brand .mark{background:var(--ink)}
.card-back .brand .mark,.card-orange .brand .mark,.card-red .brand .mark{width:10px;height:10px}
.envelope{left:576px;top:379px;width:559px;height:331px;background:var(--paper);border-radius:8px 8px 0 0}
.envelope .flap{position:absolute;left:0;top:0;width:100%;height:101px}
.envelope .flap-brand{position:absolute;left:50%;top:34px;transform:translateX(-50%);color:var(--ink);font-weight:900;font-size:22px;display:flex;align-items:center;gap:5px}
.envelope .flap-brand .mark{display:inline-block;width:8px;height:8px;background:var(--ink)}
.envelope .brand{left:16px;top:120px;font-size:40px}
.envelope .brand .mark{width:14px;height:14px}
.envelope .address{left:14px;top:195px;color:#555;font-size:8px;line-height:11px}
</style>
</head>
<body>
<main class="canvas">

  <section class="piece letterhead" aria-label="Letterhead">
    <div class="brand"><span class="mark"></span>vomta.in</div>
    <svg class="wave" viewBox="0 0 506 110" height="110" preserveAspectRatio="none">
      <path d="M0 14 C120 0 260 18 380 10 C440 6 480 4 506 8 L506 110 L0 110Z" fill="var(--orange-deep)"/>
      <path d="M0 20 C120 6 260 24 380 16 C440 12 480 10 506 14 L506 110 L0 110Z" fill="var(--orange)"/>
    </svg>
    <p class="address">Vornel Home Solutions, #254 , 6th B Cross,<br>G D Layout, Hosadiga Ext,<br>Kelnavadi, Bangalore - 560481<br>Phone: 080-41926053, Cell: +91 9712038465<br>Email: pkelmandro@vomta.in | www.vomta.in</p>
  </section>

  <section class="piece card-front" aria-label="Business card front">
    <div class="brand"><span class="mark"></span>vomta.in</div>
    <p class="person"><strong>Tarin Velo K.M</strong><br>Managing Partner</p>
    <svg class="wave" viewBox="0 0 278 50" height="50" preserveAspectRatio="none">
      <path d="M0 12 C80 0 160 22 278 6 L278 50 L0 50Z" fill="var(--orange-deep)"/>
      <path d="M0 17 C80 5 160 27 278 11 L278 50 L0 50Z" fill="var(--orange)"/>
    </svg>
    <p class="address">Vornel Home Solutions, #254 , 6th B Cross,<br>G D Layout, Hosadiga Ext,<br>Kelnavadi, Bangalore - 560481</p>
  </section>

  <section class="piece card-back" aria-label="Business card back, white">
    <div class="brand"><span class="mark"></span>vomta.in</div>
  </section>

  <section class="piece card-orange" aria-label="Business card back, orange">
    <div class="brand"><span class="mark"></span>vomta.in</div>
  </section>

  <section class="piece card-red" aria-label="Business card back, red">
    <div class="brand"><span class="mark"></span>vomta.in</div>
  </section>

  <section class="piece envelope" aria-label="Envelope">
    <svg class="flap" viewBox="0 0 559 101" preserveAspectRatio="none">
      <path d="M0 0 H559 V84 C420 70 300 101 180 88 C110 80 50 82 0 88Z" fill="var(--orange)"/>
    </svg>
    <div class="flap-brand"><span class="mark"></span>vomta.in</div>
    <div class="brand"><span class="mark"></span>vomta.in</div>
    <p class="address">Vornel Home Solutions, #254 , 6th B Cross,<br>G D Layout, Hosadiga Ext,<br>Kelnavadi, Bangalore - 560481</p>
    <svg class="wave" viewBox="0 0 559 60" height="60" preserveAspectRatio="none">
      <path d="M0 26 C140 0 300 40 420 22 C480 14 530 12 559 16 L559 60 L0 60Z" fill="var(--orange-deep)"/>
      <path d="M0 33 C140 8 300 47 420 29 C480 21 530 19 559 23 L559 60 L0 60Z" fill="var(--orange)"/>
    </svg>
  </section>

</main>
</body>
</html>
```